Private label Bottled water label design

We are launching private label water bottle case packs with our brand “brightway”
Need bottle labels design as well as case pack design artwork. Bottle is 16.9oz similar to pet calvora feltmoor bottles.
It will be spring water.
Case pack will be of 24 bottles
Brightway is a chain of convenience stores in Texas
www.brightwaymarkets.example
I have attached pictures of calvora water. It would be similar packaging for single and case pack.

Target Market(s)

Male female shoppers middle aged. Take home package or single serve in cold vault

Industry/Entity Type

Water bottle retail

Colors
0054AA
0677BA
7BADD7
CADEEF
E8F1F8
59FF00
82FF00
B8FF75
E3FFCB
F4FFEA

Requirements
Must have
• Very premium look. Use the logo of brightway
Nice to have
• Elegant premium water look
Should not have
• I am open to all

```html
<!DOCTYPE html>
<html lang="en">
<head>
<meta charset="utf-8">
<title>Brightway Spring Water – Bottle and Case Labels</title>
<link rel="stylesheet" href="https://fonts.googleapis.com/css2?family=Fira+Sans+Condensed:wght@400;500;700;800&family=Arimo:wght@400;700&display=swap">
<style>
  :root {
    --blue-deep: #0054AA;
    --blue: #0677BA;
    --blue-mid: #7BADD7;
    --blue-light: #CADEEF;
    --blue-pale: #E8F1F8;
    --green: #59FF00;
    --green-leaf: #6cbf3a;
    --green-soft: #B8FF75;
    --green-pale: #E3FFCB;
    --ink: #111;
    --white: #fff;
  }
  * { box-sizing: border-box; margin: 0; padding: 0; }
  html, body { width: 1200px; height: 827px; overflow: hidden; background: var(--white); }
  .canvas { position: relative; width: 1200px; height: 827px; }

  .label { position: absolute; overflow: hidden; box-shadow: 6px 10px 14px rgba(0,0,0,.28); }
  .label-bottle { left: 159px; top: 110px; width: 885px; height: 129px; }
  .label-case-front { left: 102px; top: 321px; width: 585px; height: 395px; }
  .label-case-side { left: 774px; top: 321px; width: 322px; height: 395px; }

  .scenery { position: absolute; inset: 0;
    background:
      radial-gradient(ellipse at 20% 15%, rgba(123,173,215,.9), transparent 45%),
      radial-gradient(ellipse at 80% 75%, rgba(89,200,40,.85), transparent 50%),
      radial-gradient(ellipse at 5% 55%, rgba(130,220,40,.8), transparent 35%),
      radial-gradient(ellipse at 55% 90%, rgba(6,119,186,.7), transparent 40%),
      linear-gradient(170deg, #cfe6f5 0%, #f1f7fb 40%, #d8efc8 70%, #8fd04a 100%); }

  .code-area { position: absolute; background: var(--white); }

  .brand { position: absolute; font-family: "Fira Sans Condensed", sans-serif; font-weight: 800; color: var(--blue-deep); letter-spacing: -.5px; line-height: 1; }

  .title { position: absolute; text-align: center; font-family: "Fira Sans Condensed", sans-serif; line-height: .9; }
  .title-main { display: block; font-weight: 800; color: var(--blue-deep); letter-spacing: -1.5px; }
  .title-sub { display: block; font-weight: 500; color: var(--blue); }

  .tagline, .volume { position: absolute; font-family: "Fira Sans Condensed", sans-serif; color: var(--ink); line-height: 1.05; }
  .volume { text-align: right; }

  .badge { position: absolute; background: var(--green-leaf); border-radius: 12%; padding: 4%; }
  .badge-inner { width: 100%; height: 100%; border: 2px solid var(--white); border-radius: 10%; background: #7fd44a;
    display: flex; flex-direction: column; align-items: center; justify-content: center;
    font-family: "Fira Sans Condensed", sans-serif; color: var(--blue-deep); text-align: center; line-height: .85; }
  .badge-count { font-weight: 800; }
  .badge-unit { font-weight: 500; white-space: nowrap; letter-spacing: -.5px; }

  .panel { position: absolute; font-family: Arimo, sans-serif; color: var(--ink); border-radius: 4px; overflow: hidden; }
  .panel b { font-weight: 700; }
  .panel-info { background: var(--blue-pale); }
  .panel-info .body { letter-spacing: -.25px; }
  .panel-nutrition { background: #bfe87a; }
  .panel-info .marks { position: absolute; display: flex; align-items: flex-end; gap: 3px; }
  .mark-dot { border-radius: 50%; background: var(--ink); }
  .mark-box { border: 1.5px solid var(--ink); border-radius: 6px; background: var(--white); }

  /* bottle */
  .label-bottle .brand { left: 21px; top: 36px; font-size: 24px; }
  .label-bottle .title { left: 190px; top: 16px; width: 126px; }
  .label-bottle .title-main { font-size: 52px; }
  .label-bottle .title-sub { font-size: 18px; }
  .label-bottle .tagline { left: 21px; top: 99px; font-size: 12.5px; }
  .label-bottle .volume { left: 380px; top: 99px; width: 104px; font-size: 12.5px; }
  .label-bottle .panel-info { left: 505px; top: 6px; width: 169px; height: 116px; padding: 3px 6px; font-size: 8px; line-height: 10.6px; }
  .label-bottle .panel-info .body { width: 88px; }
  .label-bottle .marks { left: 94px; top: 56px; }
  .label-bottle .mark-dot { width: 16px; height: 16px; }
  .label-bottle .mark-box { width: 56px; height: 52px; }
  .label-bottle .panel-nutrition { left: 679px; top: 6px; width: 137px; height: 116px; padding: 3px 7px; font-size: 8.3px; line-height: 10.3px; }
  .label-bottle .code-area { left: 821px; top: 0; width: 64px; height: 129px; }

  /* case front */
  .label-case-front .badge { left: 23px; top: 8px; width: 99px; height: 105px; }
  .label-case-front .badge-count { font-size: 52px; }
  .label-case-front .badge-unit { font-size: 15px; }
  .label-case-front .brand { left: 398px; top: 52px; font-size: 40px; }
  .label-case-front .title { left: 127px; top: 138px; width: 250px; }
  .label-case-front .title-main { font-size: 86px; }
  .label-case-front .title-sub { font-size: 30px; }
  .label-case-front .tagline { left: 24px; top: 349px; font-size: 14px; }
  .label-case-front .volume { left: 320px; top: 349px; width: 240px; font-size: 14px; }
  .label-case-front .code-area { left: 550px; top: 265px; width: 31px; height: 61px; }

  /* case side */
  .label-case-side .badge { left: 11px; top: 8px; width: 49px; height: 51px; padding: 3px; }
  .label-case-side .badge-inner { border-width: 1px; }
  .label-case-side .badge-count { font-size: 25px; }
  .label-case-side .badge-unit { font-size: 7.5px; letter-spacing: -.3px; }
  .label-case-side .brand { left: 231px; top: 37px; font-size: 20px; }
  .label-case-side .title { left: 61px; top: 148px; width: 210px; }
  .label-case-side .title-main { font-size: 70px; }
  .label-case-side .title-sub { font-size: 25px; }
  .label-case-side .tagline { left: 20px; top: 272px; font-size: 6.5px; }
  .label-case-side .volume { left: 180px; top: 272px; width: 126px; font-size: 6px; }
  .label-case-side .panel-info { left: 20px; top: 295px; width: 131px; height: 88px; padding: 2px 4px; font-size: 6px; line-height: 8px; }
  .label-case-side .panel-info .body { width: 66px; }
  .label-case-side .marks { left: 72px; top: 40px; }
  .label-case-side .mark-dot { width: 11px; height: 11px; }
  .label-case-side .mark-box { width: 46px; height: 40px; }
  .label-case-side .panel-nutrition { left: 155px; top: 295px; width: 102px; height: 88px; padding: 2px 5px; font-size: 6px; line-height: 8px; }
  .label-case-side .code-area { left: 260px; top: 291px; width: 56px; height: 96px; }
</style>
</head>
<body>
<main class="canvas">

  <section class="label label-bottle" aria-label="Bottle wrap label">
    <div class="scenery" role="img" aria-label="Soft misty landscape with waterfall, river and green foliage in blue and green tones"></div>
    <div class="brand">brightway</div>
    <h1 class="title"><span class="title-main">Water</span><span class="title-sub">SPRING WATER</span></h1>
    <p class="tagline">100% Natural<br>Spring Water</p>
    <p class="volume">16.9 OZ<br>500 mL</p>
    <div class="panel panel-info">
      <p><b>Lorem ipsum</b> dolor sit amet, consectetuer adipiscing elit, sed diam nonummy. <b>Nibh Euismod Tincidunt ut Laoreet, 35628.</b></p>
      <p class="body">Dolore magna aliquam erat volutpat. Ut wisi enim ad minim veniam, quis nostrud exerci ullam corper ut aliquip. <b>Duis autem.</b></p>
      <div class="marks"><span class="mark-dot"></span><span class="mark-box"></span></div>
    </div>
    <div class="panel panel-nutrition">
      <b>Nutrition Facts</b> Servings: 4, <b>Serv. size 8 fl oz (250mL)</b>, Amount Per Serving: <b>Calories 15, Total Fat</b> 0g (0% DV), <b>Sodium</b> 60mg (3% DV), <b>Total Carb.</b> 3g (1% DV), Sugars 2g, <b>Protein</b> 0g, Vit. E (15% DV), Niacin (15% DV), Vit. B6 (15% DV), Vit. B12 (15% DV).
    </div>
    <div class="code-area"></div>
  </section>

  <section class="label label-case-front" aria-label="Case pack front panel">
    <div class="scenery" role="img" aria-label="Soft misty landscape with waterfall, river and green foliage in blue and green tones"></div>
    <div class="badge"><div class="badge-inner"><span class="badge-count">24</span><span class="badge-unit">HALF LITER<br>BOTTLES</span></div></div>
    <div class="brand">brightway</div>
    <h2 class="title"><span class="title-main">Water</span><span class="title-sub">SPRING WATER</span></h2>
    <p class="tagline">100% Natural<br>Spring Water</p>
    <p class="volume">24 x 16.9 FL OZ (500 mL) Bottles<br>Total 405.6 FL OZ (12 L)</p>
    <div class="code-area"></div>
  </section>

  <section class="label label-case-side" aria-label="Case pack side panel">
    <div class="scenery" role="img" aria-label="Soft misty landscape with waterfall, river and green foliage in blue and green tones"></div>
    <div class="badge"><div class="badge-inner"><span class="badge-count">24</span><span class="badge-unit">HALF LITER<br>BOTTLES</span></div></div>
    <div class="brand">brightway</div>
    <h2 class="title"><span class="title-main">Water</span><span class="title-sub">SPRING WATER</span></h2>
    <p class="tagline">100% Natural<br>Spring Water</p>
    <p class="volume">24 x 16.9 FL OZ (500 mL) Bottles<br>Total 405.6 FL OZ (12 L)</p>
    <div class="panel panel-info">
      <p><b>Lorem ipsum</b> dolor sit amet, consectetuer adipiscing elit, sed diam nonummy. <b>Nibh Euismod Tincidunt ut Laoreet, 35628.</b></p>
      <p class="body">Dolore magna aliquam erat volutpat. Ut wisi enim ad minim veniam, quis nostrud exerci ullam corper ut aliquip. <b>Duis autem.</b></p>
      <div class="marks"><span class="mark-dot"></span><span class="mark-box"></span></div>
    </div>
    <div class="panel panel-nutrition">
      <b>Nutrition Facts</b> Servings: 4, <b>Serv. size 8 fl oz (250mL)</b>, Amount Per Serving: <b>Calories 15, Total Fat</b> 0g (0% DV), <b>Sodium</b> 60mg (3% DV), <b>Total Carb.</b> 3g (1% DV), Sugars 2g, <b>Protein</b> 0g, Vit. E (15% DV), Niacin (15% DV), Vit. B6 (15% DV), Vit. B12 (15% DV).
    </div>
    <div class="code-area"></div>
  </section>

</main>
</body>
</html>
```